Law Office Business Card

We need a business card design to include the following information:
Name of Firm: Lindell Law Group, P.A.
Address: 4627 Harbin Rd, Ste 215, Coral Vale, FL 32761
Phone: 561-390-5817
Fax: 561-394-7752
Website: http://www.tlindellaw.com

We Need a place for the Person's name and email address. Please start with the following:
Denise K. Halbrook, Esq.
denise@tlindellaw.com

```html
<!DOCTYPE html>
<html lang="en">
<head>
<meta charset="utf-8">
<title>Lindell Law Group – Business Card</title>
<link href="https://fonts.googleapis.com/css2?family=Marcellus&family=Marcellus+SC&display=swap" rel="stylesheet">
<style>
  :root {
    --page-bg: #e9e7e3;
    --card-bg: #ffffff;
    --gold: #b39b6c;
    --gold-light: #d9cdb5;
    --band: #bbad95;
    --band-line: #d8cfbf;
    --ink: #2e2b27;
    --white: #ffffff;
  }
  * { margin: 0; padding: 0; box-sizing: border-box; }
  html, body { width: 1200px; height: 813px; overflow: hidden; background: var(--page-bg); }
  .canvas {
    width: 1200px; height: 813px;
    display: flex; align-items: center; justify-content: center;
  }
  .card {
    position: relative;
    width: 840px; height: 480px;
    background: var(--card-bg);
    box-shadow: 0 10px 30px rgba(0,0,0,0.12);
    font-family: "Marcellus SC", serif;
    color: var(--ink);
    overflow: hidden;
  }
  .brand {
    position: absolute; left: 70px; top: 70px;
    display: flex; align-items: center; gap: 18px;
  }
  .brand-mark {
    width: 54px; height: 54px;
    border: 2px solid var(--gold);
  }
  .brand-name {
    font-size: 34px; letter-spacing: 2px; color: var(--gold);
    line-height: 1;
  }
  .divider {
    position: absolute; left: 60px; right: 60px; top: 214px;
    height: 1px; background: var(--gold-light);
  }
  .person {
    position: absolute; right: 70px; top: 168px;
    font-size: 30px; color: var(--gold); letter-spacing: 1px;
  }
  .email {
    position: absolute; right: 70px; top: 232px;
    display: flex; align-items: center; gap: 10px;
    font-size: 20px; letter-spacing: 1px;
  }
  .phones {
    position: absolute; left: 70px; top: 240px;
    list-style: none;
    font-family: "Marcellus", serif; font-size: 22px;
  }
  .phones li { display: flex; align-items: center; gap: 10px; margin-bottom: 10px; }
  .address {
    position: absolute; right: 70px; top: 292px;
    text-align: right; font-size: 24px; line-height: 1.3; letter-spacing: 0.5px;
  }
  .band {
    position: absolute; left: 0; right: 0; bottom: 0; height: 70px;
    background: var(--band);
    display: flex; align-items: center; justify-content: flex-end;
    padding-right: 70px; gap: 14px;
  }
  .band-rule {
    position: absolute; left: 0; top: 14px; width: 430px;
    height: 1px; background: var(--band-line);
  }
  .website { color: var(--white); font-size: 28px; letter-spacing: 2px; }
  .icon { flex: none; }
</style>
</head>
<body>
<div class="canvas">
  <div class="card">
    <div class="brand">
      <div class="brand-mark"></div>
      <div class="brand-name">Lindell Law Group</div>
    </div>

    <div class="person">Denise K. Halbrook, Esq.</div>
    <div class="divider"></div>

    <div class="email">
      <svg class="icon" width="20" height="14" viewBox="0 0 20 14" aria-hidden="true">
        <rect x="0.75" y="0.75" width="18.5" height="12.5" fill="none" stroke="#b39b6c" stroke-width="1.5"/>
        <path d="M1 1 L10 8 L19 1" fill="none" stroke="#b39b6c" stroke-width="1.5"/>
      </svg>
      <span>denise@tlindellaw.com</span>
    </div>

    <ul class="phones">
      <li>
        <svg class="icon" width="20" height="20" viewBox="0 0 20 20" aria-hidden="true">
          <circle cx="10" cy="10" r="9" fill="none" stroke="#b39b6c" stroke-width="1.5"/>
          <path d="M7 5 C5 7 7 12 9 13.5 C11 15 13 15 14 13.5 L12.5 12 L11 13 C9.5 12 8 10.5 7.5 9 L8.5 7.5 Z" fill="#b39b6c"/>
        </svg>
        <span>561-390-5817</span>
      </li>
      <li>
        <svg class="icon" width="20" height="20" viewBox="0 0 20 20" aria-hidden="true">
          <circle cx="10" cy="10" r="10" fill="#b39b6c"/>
          <rect x="5" y="8" width="10" height="6" fill="#fff"/>
          <rect x="7" y="5" width="6" height="3" fill="#fff"/>
        </svg>
        <span>561-394-7752</span>
      </li>
    </ul>

    <div class="address">
      4627 Harbin Rd, Ste 215<br>
      Coral Vale, FL 32761
    </div>

    <div class="band">
      <div class="band-rule"></div>
      <svg class="icon" width="24" height="24" viewBox="0 0 24 24" aria-hidden="true">
        <circle cx="12" cy="12" r="10.5" fill="none" stroke="#fff" stroke-width="1.5"/>
        <ellipse cx="12" cy="12" rx="4.5" ry="10.5" fill="none" stroke="#fff" stroke-width="1.2"/>
        <line x1="1.5" y1="12" x2="22.5" y2="12" stroke="#fff" stroke-width="1.2"/>
      </svg>
      <span class="website">www.tlindellaw.com</span>
    </div>
  </div>
</div>
</body>
</html>
```